Business Card Design

2 cards please: one for tobias and one for marguerite
Updates

Project Deadline Extended
Reason: nobody used the 2 wine labels i submitted; please work with black, red, yellow, white only, i would love black gloss raise ink on the front? something strong!

Target Market(s)

rugby fans

Industry/Entity Type

Business

Contact Information for Business Card

Oak Ladder Wine, www.domainedevalbrune.com, Tobias Valbrune, 0657314926, tobias@domainedevalbrune.com, Marguerite Valbrune, 0619472853, marguerite@domainedevalbrune.com

Requirements
Must have
• i would like TMV written as a logo on the front in a family crest type design and on the back the 2 wine labels, which are uploaded and nobody used

```html
<!DOCTYPE html>
<html lang="en">
<head>
<meta charset="utf-8">
<title>Oak Ladder Wine – Business Cards</title>
<link href="https://fonts.googleapis.com/css2?family=Felipa&family=Courier+Prime&family=PT+Serif&display=swap" rel="stylesheet">
<style>
  :root {
    --backdrop: #3b3b3d;
    --wine-red: #b81c26;
    --wine-red-deep: #94141e;
    --splash-red: #d22f40;
    --paper: #ffffff;
    --ink: #141414;
    --gold: #e8b923;
    --name-tint: #f6d9db;
  }
  * { margin: 0; padding: 0; box-sizing: border-box; }
  html, body {
    width: 1200px; height: 900px; overflow: hidden;
    background: var(--backdrop);
  }
  .stage {
    position: relative; width: 1200px; height: 900px;
    display: grid;
    grid-template-columns: 440px 440px;
    grid-template-rows: 252px 252px;
    gap: 64px 64px;
    justify-content: center;
    align-content: center;
  }

  .card {
    position: relative;
    width: 440px; height: 252px;
    background: var(--paper);
    overflow: hidden;
    box-shadow: 0 10px 26px rgba(0,0,0,.35);
  }

  /* Front */
  .front-art { position: absolute; inset: 0; width: 100%; height: 100%; }
  .front-title {
    position: absolute; left: 212px; top: 46px;
    font-family: "Felipa", cursive; font-weight: 400;
    font-size: 32px; color: var(--paper); letter-spacing: 1px;
    white-space: nowrap;
  }
  .front-name {
    position: absolute; left: 226px; top: 150px;
    font-family: "Courier Prime", monospace;
    font-size: 13px; color: var(--name-tint); letter-spacing: 1.5px;
    white-space: nowrap;
  }
  .crest {
    position: absolute; right: 22px; bottom: 18px;
    display: flex; align-items: center; gap: 8px;
  }
  .crest-mark {
    width: 14px; height: 14px; border-radius: 50%;
    background: var(--gold);
  }
  .crest-name {
    font-family: "Felipa", cursive; font-size: 22px;
    color: var(--gold); letter-spacing: 2px; line-height: 1;
  }

  /* Back */
  .back-splash {
    position: absolute; right: -40px; top: 96px;
    width: 210px; height: 170px;
    border-radius: 50% 45% 40% 55%;
    background: radial-gradient(ellipse at 50% 45%, var(--splash-red) 0%, rgba(210,47,64,.7) 45%, rgba(210,47,64,0) 72%);
  }
  .back-title {
    position: absolute; left: 18px; top: 10px;
    font-family: "Felipa", cursive; font-weight: 400;
    font-size: 29px; color: var(--ink); letter-spacing: 1px;
    white-space: nowrap;
  }
  .back-rule {
    position: absolute; left: 12px; top: 51px;
    width: 234px; height: 2px; background: var(--wine-red);
  }
  .back-name {
    position: absolute; left: 12px; top: 56px; width: 234px;
    text-align: right;
    font-family: "PT Serif", serif; font-size: 10px;
    color: var(--ink); letter-spacing: 1px;
  }
  .contact-list {
    position: absolute; left: 18px; top: 90px;
    list-style: none;
    font-family: "PT Serif", serif; font-size: 12px;
    color: var(--ink); letter-spacing: 0.6px;
  }
  .contact-list li { display: flex; align-items: center; height: 19px; white-space: nowrap; }
  .contact-icon { width: 11px; height: 11px; margin-right: 10px; flex: none; }
</style>
</head>
<body>
<main class="stage">

  <!-- Tobias: front -->
  <section class="card card--front" aria-label="Front of Tobias Valbrune's card">
    <svg class="front-art" viewBox="0 0 520 300" preserveAspectRatio="none">
      <defs>
        <linearGradient id="photoTones" x1="0" y1="0" x2="0.6" y2="1">
          <stop offset="0" stop-color="#2a0a0e"/>
          <stop offset="0.55" stop-color="#6e1219"/>
          <stop offset="1" stop-color="#8a6a2a"/>
        </linearGradient>
        <linearGradient id="redField" x1="0" y1="0" x2="1" y2="1">
          <stop offset="0" stop-color="var(--wine-red)"/>
          <stop offset="1" stop-color="var(--wine-red-deep)"/>
        </linearGradient>
      </defs>
      <rect role="img" aria-label="Photo of two glasses of red wine beside a bunch of red grapes on a wooden table"
            x="0" y="0" width="520" height="300" fill="url(#photoTones)"/>
      <path d="M225 0 C 205 120, 120 240, 0 290 L0 300 L250 300 L250 0 Z" fill="var(--paper)"/>
      <path d="M238 0 C 225 130, 140 250, 0 300 L520 300 L520 0 Z" fill="url(#redField)"/>
    </svg>
    <h1 class="front-title">Oak Ladder Wine</h1>
    <p class="front-name">Tobias Valbrune</p>
    <div class="crest"><span class="crest-mark"></span><span class="crest-name">TMV</span></div>
  </section>

  <!-- Marguerite: front -->
  <section class="card card--front" aria-label="Front of Marguerite Valbrune's card">
    <svg class="front-art" viewBox="0 0 520 300" preserveAspectRatio="none">
      <rect role="img" aria-label="Photo of two glasses of red wine beside a bunch of red grapes on a wooden table"
            x="0" y="0" width="520" height="300" fill="url(#photoTones)"/>
      <path d="M225 0 C 205 120, 120 240, 0 290 L0 300 L250 300 L250 0 Z" fill="var(--paper)"/>
      <path d="M238 0 C 225 130, 140 250, 0 300 L520 300 L520 0 Z" fill="url(#redField)"/>
    </svg>
    <h1 class="front-title">Oak Ladder Wine</h1>
    <p class="front-name">Marguerite Valbrune</p>
    <div class="crest"><span class="crest-mark"></span><span class="crest-name">TMV</span></div>
  </section>

  <!-- Tobias: back -->
  <section class="card card--back" aria-label="Back of Tobias Valbrune's card">
    <div class="back-splash" role="img" aria-label="Splash of red wine spraying across the card"></div>
    <h2 class="back-title">Oak Ladder Wine</h2>
    <div class="back-rule"></div>
    <p class="back-name">Tobias Valbrune</p>
    <ul class="contact-list">
      <li>
        <svg class="contact-icon" viewBox="0 0 12 12" aria-hidden="true">
          <circle cx="6" cy="6" r="5" fill="none" stroke="var(--ink)" stroke-width="1"/>
          <ellipse cx="6" cy="6" rx="2.2" ry="5" fill="none" stroke="var(--ink)" stroke-width="0.8"/>
          <line x1="1" y1="6" x2="11" y2="6" stroke="var(--ink)" stroke-width="0.8"/>
        </svg>
        www.domainedevalbrune.com
      </li>
      <li>
        <svg class="contact-icon" viewBox="0 0 12 12" aria-hidden="true">
          <rect x="0.5" y="2.5" width="11" height="7" fill="var(--ink)"/>
          <polyline points="0.5,2.5 6,7 11.5,2.5" fill="none" stroke="var(--paper)" stroke-width="0.9"/>
        </svg>
        tobias@domainedevalbrune.com
      </li>
      <li>
        <svg class="contact-icon" viewBox="0 0 12 12" aria-hidden="true">
          <rect x="3" y="0.5" width="6" height="11" rx="1" fill="none" stroke="var(--ink)" stroke-width="1"/>
          <line x1="5" y1="10" x2="7" y2="10" stroke="var(--ink)" stroke-width="0.8"/>
        </svg>
        0657314926
      </li>
    </ul>
  </section>

  <!-- Marguerite: back -->
  <section class="card card--back" aria-label="Back of Marguerite Valbrune's card">
    <div class="back-splash" role="img" aria-label="Splash of red wine spraying across the card"></div>
    <h2 class="back-title">Oak Ladder Wine</h2>
    <div class="back-rule"></div>
    <p class="back-name">Marguerite Valbrune</p>
    <ul class="contact-list">
      <li>
        <svg class="contact-icon" viewBox="0 0 12 12" aria-hidden="true">
          <circle cx="6" cy="6" r="5" fill="none" stroke="var(--ink)" stroke-width="1"/>
          <ellipse cx="6" cy="6" rx="2.2" ry="5" fill="none" stroke="var(--ink)" stroke-width="0.8"/>
          <line x1="1" y1="6" x2="11" y2="6" stroke="var(--ink)" stroke-width="0.8"/>
        </svg>
        www.domainedevalbrune.com
      </li>
      <li>
        <svg class="contact-icon" viewBox="0 0 12 12" aria-hidden="true">
          <rect x="0.5" y="2.5" width="11" height="7" fill="var(--ink)"/>
          <polyline points="0.5,2.5 6,7 11.5,2.5" fill="none" stroke="var(--paper)" stroke-width="0.9"/>
        </svg>
        marguerite@domainedevalbrune.com
      </li>
      <li>
        <svg class="contact-icon" viewBox="0 0 12 12" aria-hidden="true">
          <rect x="3" y="0.5" width="6" height="11" rx="1" fill="none" stroke="var(--ink)" stroke-width="1"/>
          <line x1="5" y1="10" x2="7" y2="10" stroke="var(--ink)" stroke-width="0.8"/>
        </svg>
        0619472853
      </li>
    </ul>
  </section>

</main>
</body>
</html>
```